Clean business card with logo provided

I want a card that will stand out among the masses. I need the color and image to show professionalism and yet have a family appeal showing that I only deal with win/win scenarios. The back of the card will be used to take notes about the individual so I can use that in my database entry. I like modern design but need professionalism in it also. It needs to fit my "clean, safe, and affordable housing" motto. I need to be able to write on the file and update the card details for my employees.

Target Market(s)

Investors looking to make investment income through real estate

Industry/Entity Type

Real Estate

Contact Information for Business Card

Troy Vandemark
blank address, city, st, zip code
480-555-0147
troyvandemark@quillrentals.example
www.quillrentals.example

Font styles to use
Sans Serif

Requirements
Must have
• I would like the back of the card to have lines for info. example
• Met/Visited: Date:
• Interets:
Nice to have
• I want the cards color to match the logo background color. Font with details to be san serif and black. I want the card rectangular with square corners. Standard business card size. I would like to see cards designed with both images to see which i prefer more.

```html
<!DOCTYPE html>
<html lang="en">
<head>
<meta charset="utf-8">
<title>Quill Rentals LLC — Business Card</title>
<link rel="stylesheet" href="https://fonts.googleapis.com/css2?family=Montserrat:wght@400;500&family=Open+Sans:wght@400&display=swap">
<style>
  :root {
    --teal: #2cc4d4;
    --teal-light: #5fdbe6;
    --teal-deep: #1aa9ba;
    --ink: #1b1b1d;
    --ink-soft: #2b2b2e;
    --white: #ffffff;
    --page: #e9e6e1;
  }
  * { box-sizing: border-box; margin: 0; padding: 0; }
  html, body { width: 734px; height: 1200px; overflow: hidden; }
  body {
    background: var(--page);
    font-family: "Open Sans", sans-serif;
    position: relative;
  }
  .card {
    position: absolute;
    left: 57px;
    width: 620px;
    height: 354px;
    box-shadow: 0 10px 28px rgba(0,0,0,0.18);
  }
  .card--front {
    top: 150px;
    background: linear-gradient(160deg, var(--teal-light) 0%, var(--teal) 55%, var(--teal-deep) 100%);
    color: var(--ink);
  }
  .card--back {
    top: 696px;
    background: linear-gradient(160deg, var(--ink-soft) 0%, var(--ink) 60%);
    color: var(--white);
  }
  .brand {
    position: absolute;
    display: flex;
    align-items: center;
    gap: 14px;
  }
  .card--front .brand { left: 44px; top: 70px; }
  .card--back .brand { left: 44px; top: 54px; }
  .brand__mark {
    width: 30px; height: 30px;
    border-radius: 50%;
    flex: none;
  }
  .card--front .brand__mark { background: var(--ink); }
  .card--back .brand__mark { background: var(--white); }
  .brand__name {
    font-family: "Montserrat", sans-serif;
    font-weight: 400;
    font-size: 30px;
    letter-spacing: 4px;
    line-height: 1;
  }
  .card--front .brand__name { color: var(--white); }
  .card--back .brand__name { color: var(--teal); }
  .brand__tagline {
    position: absolute;
    font-size: 11px;
    letter-spacing: 0.3px;
  }
  .card--front .brand__tagline { left: 88px; top: 112px; color: var(--white); }
  .card--back .brand__tagline { left: 88px; top: 96px; color: var(--teal); }

  .contact {
    position: absolute;
    left: 300px;
    top: 176px;
    font-family: "Montserrat", sans-serif;
  }
  .contact__name {
    font-size: 25px;
    font-weight: 400;
    color: var(--white);
    margin-bottom: 16px;
  }
  .contact__row {
    display: flex;
    align-items: center;
    gap: 9px;
    font-size: 13px;
    color: var(--ink);
    margin-bottom: 10px;
  }
  .contact__row svg { width: 14px; height: 14px; flex: none; fill: var(--ink); }

  .notes {
    position: absolute;
    left: 44px;
    top: 160px;
    width: 400px;
    font-family: "Montserrat", sans-serif;
    font-size: 15px;
  }
  .notes__row { display: flex; align-items: flex-end; gap: 8px; height: 40px; }
  .notes__label { white-space: nowrap; }
  .notes__line { flex: 1; border-bottom: 1.5px solid var(--white); margin-bottom: 4px; }
  .website {
    position: absolute;
    right: 34px;
    bottom: 34px;
    font-family: "Montserrat", sans-serif;
    font-size: 13px;
    color: var(--teal);
    white-space: nowrap;
  }
</style>
</head>
<body>
  <section class="card card--front" aria-label="Business card front">
    <div class="brand">
      <span class="brand__mark"></span>
      <span class="brand__name">QUILL RENTALS LLC</span>
    </div>
    <p class="brand__tagline">Providing clean, safe, and affordable housing</p>

    <div class="contact">
      <h1 class="contact__name">Troy Vandemark</h1>
      <p class="contact__row">
        <svg viewBox="0 0 24 24" aria-hidden="true"><path d="M12 2a7 7 0 0 0-7 7c0 5 7 13 7 13s7-8 7-13a7 7 0 0 0-7-7zm0 9.5A2.5 2.5 0 1 1 12 6.5a2.5 2.5 0 0 1 0 5z"/></svg>
        blank address, city, st, zip code
      </p>
      <p class="contact__row">
        <svg viewBox="0 0 24 24" aria-hidden="true"><path d="M2 5h20v14H2z M2 5l10 8 10-8" fill="none" stroke="#1b1b1d" stroke-width="2"/></svg>
        troyvandemark@quillrentals.example
      </p>
      <p class="contact__row">
        <svg viewBox="0 0 24 24" aria-hidden="true"><path d="M6.6 10.8a15 15 0 0 0 6.6 6.6l2.2-2.2a1 1 0 0 1 1-.25 11.4 11.4 0 0 0 3.6.6 1 1 0 0 1 1 1V20a1 1 0 0 1-1 1A17 17 0 0 1 3 4a1 1 0 0 1 1-1h3.5a1 1 0 0 1 1 1c0 1.25.2 2.45.6 3.6a1 1 0 0 1-.25 1z"/></svg>
        480-555-0147
      </p>
    </div>
  </section>

  <section class="card card--back" aria-label="Business card back">
    <div class="brand">
      <span class="brand__mark"></span>
      <span class="brand__name">QUILL RENTALS LLC</span>
    </div>
    <p class="brand__tagline">Providing clean, safe, and affordable housing</p>

    <div class="notes">
      <div class="notes__row">
        <span class="notes__label">Met:</span><span class="notes__line"></span>
        <span class="notes__label">Visited:</span><span class="notes__line"></span>
      </div>
      <div class="notes__row">
        <span class="notes__label">Interests:</span><span class="notes__line"></span>
      </div>
      <div class="notes__row">
        <span class="notes__label">Problems:</span><span class="notes__line"></span>
      </div>
    </div>

    <p class="website">www.quillrentals.example</p>
  </section>
</body>
</html>
```